Apply voucher for sale using a passer-by stopper (display on the street)

I have a photo studio (www.torvikamsel.eu) and would like to use my passer-by stopper (advertising display on the street) as an advertising medium for my photo shoot voucher sale - especially in the run-up to Christmas as a special gift idea. I thought of something funny like "You look 10 years younger in our light.
Give away a voucher and save a voucher value of € 150 - but only pay € 130. - so maybe - you must have a more interesting idea.
The poster should be in portrait format 60.5x86 cm (see picture below).

Target Market(s)

Consumer

Font styles to use
Serif

Colors

Designer to choose colors to be used in the design.

Requirements
Must have
• The passer-by stopper is intended to attract attention when driving or stopping driving. And, of course, encourage you to buy a voucher.
Nice to have
• No people need to be visible on the poster. But the poster should still
be emotional - maybe also Christmas.

```html
<!DOCTYPE html>
<html lang="en">
<head>
<meta charset="utf-8">
<title>Torvik Amsel – Christmas Gift Voucher</title>
<link href="https://fonts.googleapis.com/css2?family=Cinzel:wght@500&family=Montserrat:wght@600&family=Tinos&family=Arimo&display=swap" rel="stylesheet">
<style>
  :root {
    --ink: #000;
    --paper: #fff;
    --gold: #c9962f;
    --gold-light: #f3cf6a;
    --taupe: #b9a393;
    --grey-dark: #2b2b2b;
    --text-dark: #111;
  }
  html, body { margin: 0; padding: 0; overflow: hidden; }
  body { width: 904px; height: 1200px; background: var(--ink); }
  .poster { position: relative; width: 904px; height: 1200px; overflow: hidden; }
  .poster-art { position: absolute; inset: 0; }
  .brand {
    position: absolute; left: 0; width: 904px; top: 540px;
    text-align: center; color: var(--paper);
  }
  .brand-name {
    font-family: "Cinzel", serif; font-weight: 500;
    font-size: 56px; line-height: 1; letter-spacing: 1px; margin: 0;
  }
  .brand-role {
    font-family: "Montserrat", sans-serif; font-weight: 600;
    font-size: 20px; letter-spacing: 8px; margin-top: 8px; padding-left: 8px;
  }
  .offer-lead {
    position: absolute; left: 180px; width: 554px; top: 884px; margin: 0;
    font-family: "Tinos", serif; font-size: 26px; line-height: 33px;
    text-align: center; color: var(--text-dark);
  }
  .voucher {
    position: absolute; left: 252px; top: 1032px; width: 418px; height: 106px;
    border: 2px dotted var(--gold); box-sizing: border-box;
    font-family: "Tinos", serif; color: var(--text-dark);
  }
  .voucher-title { position: absolute; left: 68px; top: 14px; font-size: 35px; line-height: 1; }
  .voucher-price { position: absolute; left: 60px; top: 50px; font-size: 56px; line-height: 1; }
  .voucher-note {
    position: absolute; left: 198px; top: 56px;
    font-family: "Arimo", sans-serif; font-size: 18px; line-height: 23px;
  }
  .voucher-note s { text-decoration-thickness: 1.5px; }
  .web {
    position: absolute; left: 0; width: 904px; top: 1150px; text-align: center;
    font-family: "Arimo", sans-serif; font-size: 24px; color: var(--text-dark);
  }
</style>
</head>
<body>
<main class="poster">
  <svg class="poster-art" width="904" height="1200" viewBox="0 0 904 1200">
    <defs>
      <linearGradient id="photo-top" x1="0" y1="0" x2="1" y2="1">
        <stop offset="0" stop-color="#4a4a4a"/>
        <stop offset=".5" stop-color="#9a9a9a"/>
        <stop offset="1" stop-color="#3a3a3a"/>
      </linearGradient>
      <linearGradient id="photo-left" x1="0" y1="0" x2="0" y2="1">
        <stop offset="0" stop-color="#8c8c8c"/>
        <stop offset=".5" stop-color="#d8d8d8"/>
        <stop offset="1" stop-color="#6a6a6a"/>
      </linearGradient>
      <linearGradient id="photo-right" x1="0" y1="0" x2="1" y2="1">
        <stop offset="0" stop-color="#7a7a7a"/>
        <stop offset="1" stop-color="#e6e6e6"/>
      </linearGradient>
      <radialGradient id="cream-glow" cx=".5" cy=".35" r=".6">
        <stop offset="0" stop-color="#f6ecd6"/>
        <stop offset="1" stop-color="#b9a393"/>
      </radialGradient>
      <linearGradient id="gold-line" x1="0" y1="0" x2="1" y2="1">
        <stop offset="0" stop-color="#c9962f"/>
        <stop offset=".5" stop-color="#f3cf6a"/>
        <stop offset="1" stop-color="#c9962f"/>
      </linearGradient>
      <linearGradient id="ornament-tone" x1="0" y1="0" x2="0" y2="1">
        <stop offset="0" stop-color="#e2b21e"/>
        <stop offset="1" stop-color="#b8860b"/>
      </linearGradient>
    </defs>

    <rect class="backdrop" width="904" height="1200" fill="var(--ink)"/>

    <rect class="photo photo-portrait" role="img" aria-label="Black and white portrait photo of a woman in a hat"
          x="40" y="0" width="830" height="420" fill="url(#photo-top)"/>

    <polygon class="photo photo-dancer" role="img" aria-label="Black and white photo of a woman in a pleated dress"
             points="98,262 450,603 76,944 -276,603" fill="url(#photo-left)" stroke="var(--ink)" stroke-width="6"/>
    <polygon class="photo photo-bride" role="img" aria-label="Black and white photo of a bride holding a bouquet"
             points="820,262 1180,620 830,970 470,620" fill="url(#photo-right)" stroke="var(--ink)" stroke-width="6"/>

    <polygon class="band-dark" points="451,620 930,1100 451,1580 -28,1100" fill="var(--grey-dark)"/>
    <polygon class="panel-cream" points="451,660 897,1077 451,1536 11,1077" fill="url(#cream-glow)"/>

    <polygon class="diamond-edge" points="451,226 775,534 451,836 138,534" fill="var(--paper)"/>
    <polygon class="diamond" points="451,238 763,534 451,824 150,534" fill="var(--ink)"/>
    <polygon class="diamond-line" points="451,254 746,534 451,808 167,534" fill="none" stroke="url(#gold-line)" stroke-width="2"/>

    <circle class="brand-circle" cx="452" cy="466" r="54" fill="none" stroke="var(--paper)" stroke-width="6"/>

    <rect class="ornament-area" role="img" aria-label="Hanging gold Christmas baubles"
          x="694" y="850" width="166" height="280" fill="url(#ornament-tone)"/>

    <rect class="frame" x="22" y="18" width="862" height="1163" fill="none" stroke="url(#gold-line)" stroke-width="3"/>
  </svg>

  <div class="brand">
    <p class="brand-name">Torvik Amsel</p>
    <div class="brand-role">FOTOGRAF</div>
  </div>

  <p class="offer-lead">Use my photo shoot coupon sale<br>especially in the run-up to Christmas<br>as a special gift idea</p>

  <div class="voucher">
    <div class="voucher-title">GIFT VOUCHER</div>
    <div class="voucher-price">130€</div>
    <div class="voucher-note">use voucher<br>value <s>150€</s></div>
  </div>

  <div class="web">www.torvikamsel.eu</div>
</main>
</body>
</html>
```